Multi Disciplinary Health Clinic Needs a Pop Up Banner

Vantoro Wellness needs a pop up banner ( approx. 33" x 80") to use at marketing events. We offer Chiropractic, Massage Therapy, Acupuncture, Laser Therapy, Shockwave Therapy and a lot of other modalities. We have a diverse client base ranging from children to professional athletes. More info about our clinic can be found at www.vantorowellness.ca

Target Market(s)

potential patients, all age ranges, people who are in pain or are wanting to improve their health

Industry/Entity Type

Health And Wellness

Font styles to use
Sans Serif

Requirements
Must have
• our logo
• serives: chiropractic, massage therapy, shockwave, laser
• our logo colours as the basis for the colour theme
• our website address
Nice to have
• our phone number
• images from our website ( i have high resolution files of all images)
• word font that fits with our logo font
Should not have
• an abundance of spa massage pictures. we focus more on the rehabilitation of pain and injury.

```html
<!DOCTYPE html>
<html lang="en">
<head>
<meta charset="utf-8">
<title>Vantoro Wellness – Pop Up Banner</title>
<link rel="stylesheet" href="https://fonts.googleapis.com/css2?family=Arimo:wght@400;700&display=swap">
<style>
  :root{
    --brand-blue:#1667ae;
    --brand-blue-light:#2a86cc;
    --brand-blue-dark:#0f4f8c;
    --ribbon-text:#1a5fa3;
    --band-grey:#5d6269;
    --band-grey-light:#9aa0a6;
    --white:#ffffff;
    --photo-light:#ece6e1;
    --photo-mid:#b48e77;
    --photo-dark:#5a4336;
  }
  *{margin:0;padding:0;box-sizing:border-box}
  html,body{width:1200px;height:2908px;overflow:hidden;background:var(--white)}
  body{font-family:"Arimo",Arial,sans-serif}
  .banner{position:relative;width:1200px;height:2908px;overflow:hidden;background:var(--brand-blue)}
  .backdrop{position:absolute;inset:0}
  .brand{position:absolute;top:80px;left:0;width:1200px;display:flex;align-items:center;justify-content:center;gap:26px}
  .brand-dot{width:86px;height:86px;border-radius:50%;background:var(--brand-blue)}
  .brand-name{font-weight:700;font-size:96px;color:var(--brand-blue);letter-spacing:1px}
  .section-ribbon{position:absolute;top:1086px;left:0;width:820px;height:84px;background:var(--white);
    clip-path:polygon(0 0,770px 0,820px 84px,0 84px);display:flex;align-items:center;padding-left:22px}
  .section-ribbon h2{font-size:43px;font-weight:700;color:var(--ribbon-text);letter-spacing:.3px}
  .services{position:absolute;top:1300px;left:0;width:1200px;list-style:none}
  .services li{position:absolute;font-size:45px;font-weight:700;color:var(--white);white-space:nowrap}
  .services li::before{content:"•";margin-right:24px}
  .photo-strip{position:absolute;top:1976px;left:0;width:1200px;height:280px;display:flex;gap:4px}
  .photo{flex:1;height:100%}
  .photo-acupuncture{background:linear-gradient(135deg,#f2ece8,#d2a58c 55%,#b4303a)}
  .photo-neck{background:linear-gradient(135deg,#6f6a66,#d9b8a2 50%,#3a3431)}
  .photo-cupping{background:linear-gradient(135deg,#c9a488,#e8cdb8 50%,#f4efe9)}
  .contact{position:absolute;top:2370px;left:0;width:1200px;text-align:center;color:var(--white)}
  .contact-lead{font-size:43px;font-weight:700}
  .contact-line{display:flex;align-items:center;justify-content:center;gap:26px;font-weight:700;font-size:58px;height:70px}
  .contact-line svg{flex:none}
  .phone{margin-top:84px}
  .email{margin-top:54px}
  .web{margin-top:54px}
</style>
</head>
<body>
<main class="banner">
  <svg class="backdrop" width="1200" height="2908" viewBox="0 0 1200 2908">
    <defs>
      <linearGradient id="photoTone" x1="0" y1="0" x2="0.3" y2="1">
        <stop offset="0" stop-color="var(--photo-light)"/>
        <stop offset="0.18" stop-color="#cbb3a3"/>
        <stop offset="0.55" stop-color="var(--photo-mid)"/>
        <stop offset="1" stop-color="var(--photo-dark)"/>
      </linearGradient>
      <linearGradient id="fadeTop" x1="0" y1="0" x2="0" y2="1">
        <stop offset="0" stop-color="#fff" stop-opacity="1"/>
        <stop offset="1" stop-color="#fff" stop-opacity="0"/>
      </linearGradient>
      <radialGradient id="blueGlow" cx="0.45" cy="0.45" r="0.7">
        <stop offset="0" stop-color="var(--brand-blue-light)"/>
        <stop offset="1" stop-color="var(--brand-blue-dark)"/>
      </radialGradient>
      <linearGradient id="greyBand" x1="0" y1="0" x2="1" y2="1">
        <stop offset="0" stop-color="var(--band-grey-light)"/>
        <stop offset="1" stop-color="var(--band-grey)"/>
      </linearGradient>
    </defs>
    <rect class="hero-photo" role="img" aria-label="Practitioner using a steel soft-tissue tool along a patient's neck and shoulder" x="0" y="0" width="1200" height="1500" fill="url(#photoTone)"/>
    <rect x="0" y="0" width="1200" height="240" fill="url(#fadeTop)"/>
    <rect x="0" y="1450" width="1200" height="1458" fill="url(#blueGlow)"/>
    <path d="M0,775 C480,760 960,930 1200,1300 L1200,1430 C920,960 420,850 0,862 Z" fill="url(#greyBand)"/>
    <path d="M0,862 C420,850 920,960 1200,1430 L1200,2908 L0,2908 Z" fill="url(#blueGlow)"/>
    <path d="M0,775 C480,760 960,930 1200,1300" fill="none" stroke="var(--white)" stroke-width="4"/>
    <path d="M0,862 C420,850 920,960 1200,1430" fill="none" stroke="var(--white)" stroke-width="3"/>
    <path d="M0,1952 Q600,1936 1200,1952 L1200,1980 L0,1980 Z" fill="var(--white)"/>
    <path d="M0,2252 L1200,2252 L1200,2270 Q600,2300 0,2270 Z" fill="var(--white)"/>
    <path d="M0,2270 Q600,2300 1200,2270 L1200,2292 Q600,2322 0,2292 Z" fill="var(--band-grey)"/>
  </svg>

  <header class="brand">
    <span class="brand-dot"></span>
    <span class="brand-name">Vantoro Wellness</span>
  </header>

  <div class="section-ribbon"><h2>GENERAL SERVICES OFFERED</h2></div>

  <ul class="services">
    <li style="top:0;left:62px">Chiropractic</li>
    <li style="top:120px;left:62px">Massage</li>
    <li style="top:242px;left:62px">Acupuncture</li>
    <li style="top:362px;left:62px">Shockwave</li>
    <li style="top:484px;left:62px">Laser Therapy</li>
    <li style="top:0;left:543px">Active Release</li>
    <li style="top:120px;left:543px">Kinesiology Tape</li>
    <li style="top:242px;left:543px">Veltra Technique</li>
    <li style="top:362px;left:543px">Cupping Technology</li>
  </ul>

  <section class="photo-strip">
    <div class="photo photo-acupuncture" role="img" aria-label="Acupuncture needle being placed in a patient's forearm"></div>
    <div class="photo photo-neck" role="img" aria-label="Practitioner's hands supporting a patient's neck during treatment"></div>
    <div class="photo photo-cupping" role="img" aria-label="Glass cupping cups being applied to a patient's back"></div>
  </section>

  <section class="contact">
    <p class="contact-lead">For More Information Please Contact Us:</p>
    <p class="contact-line phone">
      <svg width="46" height="40" viewBox="0 0 46 40" aria-hidden="true"><path d="M4 14 Q23 -2 42 14 L38 20 L31 17 L30 11 Q23 8 16 11 L15 17 L8 20 Z" fill="#fff"/><rect x="9" y="20" width="28" height="18" rx="3" fill="#fff"/><circle cx="23" cy="29" r="5" fill="var(--brand-blue)"/></svg>
      <span>(403) 555-0147</span>
    </p>
    <p class="contact-line email">
      <svg width="50" height="34" viewBox="0 0 50 34" aria-hidden="true"><rect x="2" y="2" width="46" height="30" fill="none" stroke="#fff" stroke-width="4"/><path d="M2 2 L25 20 L48 2" fill="none" stroke="#fff" stroke-width="4"/></svg>
      <span>info@vantorowellness.ca</span>
    </p>
    <p class="contact-line web">
      <svg width="44" height="44" viewBox="0 0 44 44" aria-hidden="true" fill="none" stroke="#fff" stroke-width="3.5"><circle cx="22" cy="22" r="19"/><ellipse cx="22" cy="22" rx="8" ry="19"/><path d="M3 22 H41 M7 12 H37 M7 32 H37"/></svg>
      <span>http://www.vantorowellness.ca/</span>
    </p>
  </section>
</main>
</body>
</html>
```